Business Card Design

We need a business card design for a consulting firm which provides safety and risk management consulting services for public venues, hotels and tourist attractions. The business card design should include the attached logo unedited with a design based on incorporating the existing logo with a design of geometric patterns or lines on a predominantly white background.

Industry/Entity Type

Business

Contact Information for Business Card

Dane Morravik
Director & Principal Consultant

Ph: +61 (0) 478506 214
PO Box 456 Brenmoor Vale, NSW Australia 2611
info@corvalrisksafety.example

(back of card to include website www.corvalrisksafety.example

```html
<!DOCTYPE html>
<html lang="en">
<head>
<meta charset="utf-8">
<title>Corval Risk &amp; Safety — Business Card</title>
<link href="https://fonts.googleapis.com/css2?family=Oswald:wght@400;500&family=Russo+One&display=swap" rel="stylesheet">
<style>
  :root {
    --stage: #e6e6e4;
    --card-white: #ffffff;
    --card-dark: #232323;
    --brand-green: #7cc245;
    --brand-blue: #2f8fcf;
    --title-blue: #4fa8dc;
    --ink: #3a3a3a;
    --ink-soft: #555555;
    --back-mark: #707070;
    --back-url: #5e5e5e;
  }
  * { box-sizing: border-box; margin: 0; padding: 0; }
  html, body {
    width: 1200px; height: 871px; overflow: hidden;
    background: var(--stage);
  }
  .stage { position: relative; width: 1200px; height: 871px; }

  .card {
    position: absolute; top: 281px;
    width: 540px; height: 309px; overflow: hidden;
    box-shadow: 0 6px 20px rgba(0,0,0,0.18);
  }

  /* Back side */
  .card-back { left: 40px; background: var(--card-dark); }
  .card-back .stripe-green {
    position: absolute; left: 0; top: 0; width: 56%; height: 12px;
    background: var(--brand-green);
  }
  .card-back .stripe-blue {
    position: absolute; right: 0; bottom: 0; width: 45%; height: 12px;
    background: var(--brand-blue);
  }
  .back-brand {
    position: absolute; left: 0; right: 0; top: 108px;
    display: flex; align-items: center; justify-content: center; gap: 12px;
  }
  .back-brand .mark-dot {
    width: 34px; height: 34px; border-radius: 50%;
    background: var(--back-mark);
  }
  .back-brand .brand-name {
    font-family: "Oswald", sans-serif; font-weight: 500;
    font-size: 38px; letter-spacing: 1px; color: var(--back-mark);
    text-transform: uppercase;
  }
  .back-url {
    position: absolute; left: 0; right: 0; top: 178px; text-align: center;
    font-family: "Oswald", sans-serif; font-weight: 500;
    font-size: 17px; letter-spacing: 1px; color: var(--back-url);
  }

  /* Front side */
  .card-front { left: 620px; background: var(--card-white); }
  .front-bar-green {
    position: absolute; left: 62px; top: 0; width: 38px; height: 82px;
    background: var(--brand-green);
  }
  .front-band-blue {
    position: absolute; left: 14px; top: 160px; width: 36px; height: 149px;
    background: var(--brand-blue);
  }
  .front-brand {
    position: absolute; right: 26px; top: 40px;
    display: flex; align-items: center; gap: 8px;
  }
  .front-brand .mark-dot {
    width: 20px; height: 20px; border-radius: 50%;
    background: var(--brand-blue);
  }
  .front-brand .brand-name {
    font-family: "Oswald", sans-serif; font-weight: 500;
    font-size: 21px; letter-spacing: 0.5px; color: var(--brand-blue);
    text-transform: uppercase;
  }
  .holder-name {
    position: absolute; left: 58px; top: 106px;
    font-family: "Russo One", sans-serif; font-size: 25px;
    color: var(--ink); letter-spacing: 0.5px;
  }
  .holder-title {
    position: absolute; left: 58px; top: 138px;
    font-family: "Oswald", sans-serif; font-weight: 400; font-size: 15px;
    color: var(--ink-soft);
  }
  .holder-title .role-director { color: var(--brand-green); }
  .holder-title .role-consultant { color: var(--title-blue); }

  .contact-list { list-style: none; }
  .contact-item {
    position: absolute; left: 20px; height: 24px;
    display: flex; align-items: center; gap: 18px;
    font-family: "Oswald", sans-serif; font-size: 14px; color: var(--ink-soft);
  }
  .contact-item svg { width: 24px; height: 24px; flex: none; }
  .contact-phone { top: 170px; }
  .contact-address { top: 210px; }
  .contact-email { top: 250px; }
</style>
</head>
<body>
<main class="stage">

  <section class="card card-back" aria-label="Business card, back">
    <div class="stripe-green"></div>
    <div class="stripe-blue"></div>
    <div class="back-brand">
      <span class="mark-dot"></span>
      <span class="brand-name">Corval Risk &amp; Safety</span>
    </div>
    <p class="back-url">www.corvalrisksafety.example</p>
  </section>

  <section class="card card-front" aria-label="Business card, front">
    <div class="front-bar-green"></div>
    <div class="front-band-blue"></div>

    <div class="front-brand">
      <span class="mark-dot"></span>
      <span class="brand-name">Corval Risk &amp; Safety</span>
    </div>

    <h1 class="holder-name">Dane Morravik</h1>
    <p class="holder-title"><span class="role-director">Director</span> &amp; <span class="role-consultant">Principal Consultant</span></p>

    <ul class="contact-list">
      <li class="contact-item contact-phone">
        <svg viewBox="0 0 24 24" aria-hidden="true">
          <circle cx="12" cy="12" r="12" fill="#fff"/>
          <path d="M6 10.5c0-2 2.5-3 6-3s6 1 6 3l-2 .6-1-1.6h-6l-1 1.6z" fill="#333"/>
          <rect x="8" y="11.5" width="8" height="5.5" rx="1" fill="#333"/>
        </svg>
        <span>+61 (0) 478506 214</span>
      </li>
      <li class="contact-item contact-address">
        <svg viewBox="0 0 24 24" aria-hidden="true">
          <circle cx="12" cy="12" r="12" fill="#fff"/>
          <path d="M12 5a4.5 4.5 0 0 0-4.5 4.5c0 3.4 4.5 9 4.5 9s4.5-5.6 4.5-9A4.5 4.5 0 0 0 12 5z" fill="#333"/>
          <circle cx="12" cy="9.5" r="1.7" fill="#fff"/>
        </svg>
        <span>PO Box 456 Brenmoor Vale, NSW Australia 2611</span>
      </li>
      <li class="contact-item contact-email">
        <svg viewBox="0 0 24 24" aria-hidden="true">
          <circle cx="12" cy="12" r="12" fill="#fff"/>
          <rect x="6" y="8" width="12" height="8.5" fill="#333"/>
          <path d="M6 8l6 5 6-5" fill="none" stroke="#fff" stroke-width="1"/>
        </svg>
        <span>info@corvalrisksafety.example</span>
      </li>
    </ul>
  </section>

</main>
</body>
</html>
```